Wordpress website update with basic ecomm features

We need an update to our existing website
www.quillharbour.com.au that can be easily updated, enhances our logo and can take payments online and a basic text logo suite for 3 products. Website would reflect confidence and give clients confidence in the outcomes we will provide for them. must be easy to use, crisp, fresh, clean and dynamic.

Target Market(s)

entrepreneurs, professionals, small business owners, corporate organisations, universities

Industry/Entity Type

Online

Coding

Coded - Design and coding required

Number of Pages Required

5+ page

Font styles to use
Sans Serif

Requirements
Must have
• be easy to navigate, look professional, please see brief doc
Nice to have
• please see briefing doc
Should not have
• please see briefing doc

```html
<!DOCTYPE html>
<html lang="en">
<head>
<meta charset="utf-8">
<title>Quill Harbour</title>
<link href="https://fonts.googleapis.com/css2?family=Lato:ital,wght@0,400;0,700;0,900;1,400&display=swap" rel="stylesheet">
<style>
:root{
  --ink:#1b1b1b;
  --dark:#222222;
  --darker:#161616;
  --text:#333333;
  --muted:#666666;
  --light:#f1f1f1;
  --line:#cfcfcf;
  --white:#ffffff;
}
*{box-sizing:border-box;margin:0;padding:0}
html,body{width:1200px;height:3758px;overflow:hidden}
body{font-family:'Lato',Arial,sans-serif;color:var(--text);background:var(--white);position:relative}
.abs{position:absolute}
section,header,footer{position:absolute;left:0;width:1200px;overflow:hidden}

/* header */
.site-header{top:0;height:138px;background:#f4f4f4}
.topbar{position:absolute;left:726px;top:0;width:374px;height:32px;background:var(--dark);display:flex;align-items:center;gap:10px;padding-left:22px;color:var(--white);font-size:13px;font-weight:700}
.social-dot{width:12px;height:12px;border-radius:50%;background:#bbb;display:inline-block}
.topbar .btn{background:#3a3a3a;padding:5px 12px;font-weight:400;margin-left:6px}
.brand{position:absolute;left:113px;top:22px;display:flex;align-items:center;gap:12px}
.brand-square{width:44px;height:44px;background:var(--ink);border-radius:6px}
.brand-name{font-size:20px;font-weight:700;color:var(--ink);letter-spacing:1px;text-transform:uppercase}
.main-nav{position:absolute;right:100px;top:80px;display:flex;gap:36px;font-size:14px;color:var(--ink)}
.main-nav .current{font-weight:700}

.hero{top:138px;height:518px;background:linear-gradient(120deg,#e9ecef 0%,#c7ccd2 30%,#3a4350 55%,#d9dde2 75%,#f1f2f4 100%)}
.hero-caption{position:absolute;left:100px;top:355px;width:639px;background:rgba(20,20,20,.88);color:var(--white);font-size:22px;line-height:31px;padding:12px 22px;font-weight:700}

/* headings */
.sec-title{position:absolute;left:0;width:1200px;text-align:center;font-size:30px;color:var(--ink)}
.sec-title b{font-weight:900}
.divider{position:absolute;left:400px;width:400px;height:16px}
.divider::before{content:"";position:absolute;left:0;right:0;top:8px;height:1px;background:var(--line)}
.divider::after{content:"";position:absolute;left:192px;top:0;width:16px;height:16px;background:#d6d6d6;border:2px solid #fff;outline:1px solid #bbb}
.btn-dark{position:absolute;background:var(--ink);color:var(--white);font-size:13px;font-weight:700;text-align:center;line-height:30px}

.about{top:656px;height:296px}
.about p{position:absolute;left:130px;width:940px;top:130px;text-align:center;font-size:13px;line-height:19px}

.pillars{top:952px;height:401px;display:flex}
.pillar{width:400px;height:401px;position:relative;color:var(--white);text-align:center}
.pillar:nth-child(1){background:linear-gradient(180deg,#3a3a3a,#1f1f1f)}
.pillar:nth-child(2){background:linear-gradient(180deg,#4b4b4b,#2a2a2a)}
.pillar:nth-child(3){background:linear-gradient(180deg,#353535,#1c1c1c)}
.pillar .ring{position:absolute;left:142px;top:55px;width:116px;height:116px;border:3px solid var(--white);border-radius:50%}
.pillar svg{position:absolute;left:170px;top:83px}
.pillar h3{position:absolute;top:188px;width:100%;font-size:20px;font-weight:700}
.pillar p{position:absolute;top:222px;left:90px;width:220px;font-size:13px;line-height:17px}
.pillar .more{position:absolute;left:158px;top:320px;width:84px;height:32px;border:1px solid #bbb;font-size:12px;line-height:30px}

.deliver{top:1353px;height:626px;background:var(--light)}
.hub-ring{position:absolute;left:0;top:0}
.node{position:absolute;width:74px;height:74px;border-radius:50%;background:var(--ink);border:4px solid var(--light)}
.node svg{position:absolute;left:17px;top:17px}
.label{position:absolute;font-size:16px;font-weight:700;color:var(--ink);line-height:21px}
.label.r{text-align:right}
.hub-square{position:absolute;left:536px;top:338px;width:145px;height:145px;background:var(--ink);border-radius:10px}
.hub-name{position:absolute;left:456px;top:496px;width:305px;text-align:center;font-size:15px;letter-spacing:4px;color:var(--ink);text-transform:uppercase}

.programs{top:1979px;height:225px;background:linear-gradient(90deg,#1a1a1a,#2b2622 50%,#1a1a1a)}
.prog{position:absolute;top:50px;width:318px;text-align:center;color:#eee;font-style:italic;font-size:13px;line-height:18px}
.prog .box{margin-top:16px;height:85px;background:var(--white);border-radius:3px;display:flex;align-items:center;justify-content:center;font-style:normal;color:var(--ink)}
.prog .product{font-size:34px;font-weight:700}
.prog .blurb{font-size:17px;line-height:22px;padding:0 30px}

.events{top:2204px;height:401px}
.card{position:absolute;top:138px;width:318px;height:218px;border:1px solid #ddd}
.card .photo{height:186px}
.card .date{position:absolute;left:0;top:0;background:rgba(20,20,20,.85);color:var(--white);font-size:12px;padding:4px 8px;line-height:18px}
.card .date b{display:block;font-size:16px}
.card .cap{text-align:center;font-size:13px;line-height:31px}

.split{top:2605px;height:413px;background:var(--light)}
.col-title{position:absolute;top:55px;font-size:30px;color:var(--ink)}
.col-title b{font-weight:900}
.mini-line{position:absolute;top:97px;height:16px;width:471px}
.mini-line::before{content:"";position:absolute;left:24px;right:0;top:8px;height:1px;background:var(--line)}
.mini-line::after{content:"";position:absolute;left:0;top:0;width:16px;height:16px;background:#d6d6d6}
.testis{position:absolute;left:100px;top:138px;width:471px;height:213px;background:#e4e4e4}
.testi{position:absolute;left:20px;display:flex;gap:16px;font-size:13px;line-height:17px;width:440px}
.testi .av{width:56px;height:56px;border-radius:50%;background:#9a9a9a;border:3px solid #fff;flex:none}
.testi b{display:block;margin-bottom:3px}
.faq{position:absolute;left:626px;width:476px}
.faq-item{height:34px;background:#e2e2e2;margin-bottom:11px;font-size:13px;font-weight:700;line-height:34px;padding-left:12px;position:relative}
.faq-item::after{content:"+";position:absolute;right:10px;top:9px;width:16px;height:16px;border-radius:50%;background:#555;color:#fff;font-size:14px;line-height:15px;text-align:center}
.faq-item.open{background:var(--ink);color:var(--white);margin-bottom:0}
.faq-item.open::after{content:"−";background:#fff;color:#222}
.faq-body{background:var(--white);border:1px solid #ccc;padding:10px 12px;font-size:12px;line-height:16px;height:64px}

.say{top:3018px;height:409px}
.say .quote{position:absolute;left:150px;width:900px;top:146px;text-align:center;font-style:italic;font-size:13px;line-height:19px}
.say .qmark{position:absolute;font-size:70px;color:#ccc;font-family:Georgia,serif;line-height:1}
.say .rule{position:absolute;left:250px;width:700px;top:239px;height:1px;background:var(--line)}
.say .av{position:absolute;top:284px;width:70px;height:70px;border-radius:50%;background:#a5a5a5;border:3px solid #ddd}
.say .name{position:absolute;top:347px;width:1200px;text-align:center;font-size:14px;font-weight:700}

.site-footer{top:3427px;height:293px;background:var(--darker);color:#ddd}
.fcol{position:absolute;top:45px}
.fcol h4{font-size:16px;font-weight:700;color:var(--white);padding-bottom:10px;border-bottom:1px solid #444;margin-bottom:14px}
.links{list-style:none;font-size:12px;line-height:26px}
.links li::before{content:"▸ ";font-size:9px;color:#aaa}
.contact-row{display:flex;gap:18px;font-size:13px;line-height:18px;margin-bottom:18px}
.contact-row svg{flex:none;margin-top:2px}
.field{width:240px;height:32px;background:var(--white);margin-bottom:8px;color:#999;font-size:12px;padding:8px 10px}
.field.tall{height:56px}
.submit{width:100px;height:32px;background:#000;color:#fff;font-size:13px;font-weight:700;text-align:center;line-height:32px}
.foot-brand{position:absolute;left:952px;top:85px;text-align:center;width:146px}
.foot-brand .sq{width:90px;height:90px;background:var(--white);border-radius:10px;margin:0 auto 10px}
.foot-brand span{font-size:13px;letter-spacing:3px;color:var(--white)}
.copyright{position:absolute;left:0;top:3720px;width:1200px;height:38px;background:#0b0b0b;color:#bbb;font-size:12px;text-align:center;line-height:38px}
</style>
</head>
<body>

<header class="site-header">
  <div class="topbar">Follow Us :
    <span class="social-dot"></span><span class="social-dot"></span><span class="social-dot"></span><span class="social-dot"></span>
    <span class="btn">Login</span><span class="btn">Register</span>
  </div>
  <div class="brand"><span class="brand-square"></span><span class="brand-name">Quill Harbour</span></div>
  <nav class="main-nav">
    <span class="current">Home</span><span>About</span><span>Programs</span><span>Events</span><span>Why Quill Harbour</span><span>FAQ</span><span>Contact Us</span>
  </nav>
</header>

<section class="hero" role="img" aria-label="Business people shaking hands around a meeting table in a bright office">
  <div class="hero-caption">Builds And Develops Validation And Innovation Programs, Communities And Data To Improve The Overall Success.</div>
</section>

<section class="about">
  <h2 class="sec-title" style="top:48px"><b>About</b> Quill Harbour</h2>
  <div class="divider" style="top:88px"></div>
  <p>Quill Harbour builds and develops validation and innovation programs, communities and data to improve the overall success rate of entrepreneurial and early-stage ventures. Our aim is to build a flourishing innovation and collaboration eco-system that validates people, business &amp; society. Quill Harbour takes the value created from the 4 early stage venture institutions</p>
  <div class="btn-dark" style="left:543px;top:222px;width:112px">Read More</div>
</section>

<section class="pillars">
  <div class="pillar">
    <div class="ring"></div>
    <svg width="60" height="60" viewBox="0 0 60 60" fill="none" stroke="#fff" stroke-width="3"><path d="M6 30 Q30 8 54 30 Q30 52 6 30Z"/><circle cx="30" cy="30" r="8" fill="#fff"/></svg>
    <h3>Our Vision</h3>
    <p>Lorem ipsum dolor sit amet, consectetur adipiscing elit, sed diam nonummy nibh euismod tincidunt ut</p>
    <div class="more">Read More</div>
  </div>
  <div class="pillar">
    <div class="ring"></div>
    <svg width="60" height="60" viewBox="0 0 60 60" fill="none" stroke="#fff" stroke-width="3"><path d="M4 26 L16 18 L28 24 L36 20 L56 26"/><path d="M14 30 L26 42 Q30 44 32 40 L44 32"/><path d="M20 36 L30 46"/></svg>
    <h3>Our Value</h3>
    <p>Lorem ipsum dolor sit amet, consectetuer adipiscing elit, sed diam nonummy nibh euismod tincidunt ut</p>
    <div class="more">Read More</div>
  </div>
  <div class="pillar">
    <div class="ring"></div>
    <svg width="60" height="60" viewBox="0 0 60 60" fill="none" stroke="#fff" stroke-width="3"><circle cx="28" cy="32" r="22"/><circle cx="28" cy="32" r="13"/><circle cx="28" cy="32" r="4" fill="#fff"/><path d="M28 32 L52 8 M46 8 H52 V14"/></svg>
    <h3>Our Mission</h3>
    <p>Lorem ipsum dolor sit amet, consectetuer adipiscing elit, sed diam nonummy nibh euismod tincidunt ut</p>
    <div class="more">Read More</div>
  </div>
</section>

<section class="deliver">
  <h2 class="sec-title" style="top:40px"><b>What</b> We Deliver</h2>
  <div class="divider" style="top:80px"></div>
  <svg class="hub-ring" width="1200" height="626"><circle cx="606" cy="420" r="228" fill="none" stroke="#1b1b1b" stroke-width="10"/></svg>

  <div class="node" style="left:504px;top:173px"><svg width="32" height="32" viewBox="0 0 32 32" fill="#fff" stroke="#fff" stroke-width="2"><circle cx="8" cy="16" r="4"/><circle cx="24" cy="7" r="4"/><circle cx="24" cy="25" r="4"/><path d="M8 16 L24 7 M8 16 L24 25"/></svg></div>
  <div class="node" style="left:629px;top:173px"><svg width="32" height="32" viewBox="0 0 32 32" fill="#fff"><circle cx="16" cy="4" r="3"/><circle cx="28" cy="16" r="3"/><circle cx="16" cy="28" r="3"/><circle cx="4" cy="16" r="3"/><circle cx="16" cy="16" r="9" fill="none" stroke="#fff" stroke-width="2"/></svg></div>
  <div class="node" style="left:401px;top:233px"><svg width="32" height="32" viewBox="0 0 32 32" fill="none" stroke="#fff" stroke-width="3"><path d="M8 12 L14 4 L20 12 M26 14 L28 24 L18 26 M6 24 L4 16"/></svg></div>
  <div class="node" style="left:732px;top:233px"><svg width="32" height="32" viewBox="0 0 32 32" fill="none" stroke="#fff" stroke-width="3"><path d="M2 14 L10 10 L18 14 L24 10 L30 14 M8 18 L16 26 L24 18"/></svg></div>
  <div class="node" style="left:349px;top:328px"><svg width="32" height="32" viewBox="0 0 32 32" fill="#fff"><circle cx="10" cy="9" r="5"/><circle cx="22" cy="9" r="5"/><rect x="3" y="17" width="12" height="12" rx="3"/><rect x="17" y="17" width="12" height="12" rx="3"/></svg></div>
  <div class="node" style="left:790px;top:328px"><svg width="32" height="32" viewBox="0 0 32 32" fill="#fff"><circle cx="10" cy="7" r="4"/><circle cx="22" cy="7" r="4"/><rect x="6" y="13" width="8" height="17" rx="2"/><rect x="18" y="13" width="8" height="17" rx="2"/></svg></div>
  <div class="node" style="left:339px;top:426px"><svg width="32" height="32" viewBox="0 0 32 32" fill="#fff"><circle cx="16" cy="8" r="5"/><circle cx="6" cy="12" r="4"/><circle cx="26" cy="12" r="4"/><rect x="9" y="15" width="14" height="12" rx="3"/><rect x="1" y="18" width="9" height="9" rx="3"/><rect x="22" y="18" width="9" height="9" rx="3"/></svg></div>
  <div class="node" style="left:797px;top:426px"><svg width="32" height="32" viewBox="0 0 32 32" fill="#fff"><circle cx="12" cy="7" r="5"/><rect x="6" y="14" width="12" height="16" rx="3"/><path d="M20 12 L30 4" stroke="#fff" stroke-width="2"/></svg></div>
  <div class="node" style="left:384px;top:519px"><svg width="32" height="32" viewBox="0 0 32 32" fill="none" stroke="#fff" stroke-width="2.5"><rect x="10" y="4" width="20" height="16"/><circle cx="6" cy="14" r="3" fill="#fff"/><path d="M4 30 V20 H10"/></svg></div>
  <div class="node" style="left:752px;top:519px"><svg width="32" height="32" viewBox="0 0 32 32" fill="#fff"><circle cx="16" cy="7" r="4"/><circle cx="6" cy="17" r="4"/><circle cx="26" cy="17" r="4"/><circle cx="16" cy="24" r="4"/></svg></div>

  <div class="label r" style="right:692px;top:150px">Shared Resourcing</div>
  <div class="label" style="left:706px;top:150px">Powerful Networks</div>
  <div class="label r" style="right:812px;top:234px">Venture, Personal &amp; Social<br>Outcomes</div>
  <div class="label" style="left:827px;top:234px">Investment &amp; Industry<br>Partnerships</div>
  <div class="label r" style="right:864px;top:352px">Real Collaboration</div>
  <div class="label" style="left:882px;top:340px">Informal And Formal<br>Meet-ups</div>
  <div class="label r" style="right:872px;top:452px">Expert Facilitation</div>
  <div class="label" style="left:887px;top:452px">Coaching</div>
  <div class="label r" style="right:829px;top:552px">Best Practice Business Education</div>
  <div class="label" style="left:845px;top:552px">Community</div>

  <div class="hub-square"></div>
  <div class="hub-name">Quill Harbour</div>
</section>

<section class="programs">
  <div class="prog" style="left:100px">The Experienced Economy<br>Shared Learning &amp; Opportunities
    <div class="box"><span class="product">Spark Start</span></div></div>
  <div class="prog" style="left:443px">The Future of Business<br>Business Validation &amp; Innovation Program
    <div class="box"><span class="product">Harbour Pool</span></div></div>
  <div class="prog" style="left:784px">The Power of Collaboration Business<br>Improvement &amp; Commercialisation Community
    <div class="box"><span class="blurb">Validation and innovation programs, data and communities.</span></div></div>
</section>

<section class="events">
  <h2 class="sec-title" style="top:42px"><b>Upcoming</b> Events</h2>
  <div class="divider" style="top:92px"></div>
  <div class="card" style="left:100px"><div class="photo" role="img" aria-label="Workshop attendees seated at tables in a training room" style="background:linear-gradient(135deg,#c9c4bc,#6e6a66)"></div><div class="date">04 Oct<b>2016</b></div><div class="cap">Lorem Ipsum Dolor Sit Amet</div></div>
  <div class="card" style="left:441px"><div class="photo" role="img" aria-label="Audience raising a hand at a seminar" style="background:linear-gradient(135deg,#d8b08a,#2a1f18)"></div><div class="date">04 Oct<b>2016</b></div><div class="cap">Lorem Ipsum Dolor Sit Amet</div></div>
  <div class="card" style="left:782px"><div class="photo" role="img" aria-label="Conference hall audience facing a presentation screen" style="background:linear-gradient(160deg,#7b8fa8,#8a5a3c 60%,#4a3226)"></div><div class="date">04 Oct<b>2016</b></div><div class="cap">Lorem Ipsum Dolor Sit Amet</div></div>
</section>

<section class="split">
  <h2 class="col-title" style="left:100px">Client <b>Testimonials</b></h2>
  <div class="mini-line" style="left:100px"></div>
  <div class="testis">
    <div class="testi" style="top:22px"><span class="av"></span><div><b>Clara J. Redmond-WA</b>Lorem ipsum dolor sit amet, consectetur adipiscing elit, sed eiusmod tempor incididunt ut labore et dolore magna aliqua.</div></div>
    <div class="testi" style="top:120px"><span class="av"></span><div><b>Nora P. Everett-WA</b>Lorem ipsum dolor sit amet, consectetur adipiscing elit, sed eiusmod tempor incididunt ut labore et dolore magna aliqua.</div></div>
  </div>
  <h2 class="col-title" style="left:626px"><b>FAQ</b></h2>
  <div class="mini-line" style="left:626px"></div>
  <div class="faq" style="top:138px">
    <div class="faq-item">1. Duis aute irure dolor in reprehenderit in voluptate ?</div>
    <div class="faq-item">2. Neque porro quisquam est, qui dolorem ?</div>
    <div class="faq-item">3. Nemo enim ipsam voluptatem quia voluptas sit ?</div>
    <div class="faq-item open">4. Excepteur sint occaecat cupidatat non proident ?</div>
    <div class="faq-body">Lorem ipsum dolor sit amet, consectetur adipiscing elit, sed do eiusmod tempor incididunt ut labore et dolore magna aliqua. Ut enim ad minim</div>
  </div>
</section>

<section class="say">
  <h2 class="sec-title" style="top:40px"><b>What People Say About Us!</b></h2>
  <div class="divider" style="top:98px"></div>
  <span class="qmark" style="left:150px;top:120px">&ldquo;</span>
  <p class="quote">Lorem ipsum dolor sit amet, consectetur adipiscing elit, sed do eiusmod tempor incididunt ut labore et dolore magna aliqua. Ut enim ad minim veniam, quis nostrud exercitation ullamco laboris nisi ut aliquip ex ea commodo consequat. Duis aute irure dolor in reprehenderit in voluptate velit esse cillum dolore eu fugiat nulla pariatur. Excepteur sint occaecat cupidatat non proident, sunt in culpa qui</p>
  <span class="qmark" style="left:1010px;top:178px">&rdquo;</span>
  <div class="rule"></div>
  <span class="av" style="left:471px"></span>
  <span class="av" style="left:566px;border-color:#fff;background:#b8a899"></span>
  <span class="av" style="left:659px"></span>
  <div class="name">Lorem Ipsum</div>
</section>

<footer class="site-footer">
  <div class="fcol" style="left:100px;width:120px">
    <h4>Quick Link</h4>
    <ul class="links"><li>Home</li><li>About</li><li>Programs</li><li>Events</li><li>Why Quill Harbour</li><li>FAQ</li><li>Contact Us</li></ul>
  </div>
  <div class="fcol" style="left:288px;width:180px">
    <h4>Contact Information</h4>
    <div class="contact-row"><svg width="12" height="16" viewBox="0 0 12 16" fill="#ddd"><path d="M6 0A6 6 0 0 0 0 6C0 10 6 16 6 16S12 10 12 6A6 6 0 0 0 6 0ZM6 8A2 2 0 1 1 6 4A2 2 0 0 1 6 8Z"/></svg><div><b>Quill Harbour</b><br>2a Mattis porttitor nulla, eget eleifend metus gravida id</div></div>
    <div class="contact-row"><svg width="14" height="14" viewBox="0 0 14 14" fill="#ddd"><path d="M3 0L5 4L3.5 5.5Q5 8.5 8.5 10.5L10 9L14 11L13 14Q5 13 0 1Z"/></svg><div>123.456.7890</div></div>
    <div class="contact-row"><svg width="14" height="12" viewBox="0 0 14 12" fill="none" stroke="#ddd" stroke-width="1.5"><rect x="1" y="1" width="12" height="10"/><path d="M1 1L7 6L13 1"/></svg><div>info@quillharbour.com.au</div></div>
  </div>
  <div class="fcol" style="left:646px;width:240px">
    <h4>Quick Inquiry</h4>
    <div class="field">Name</div>
    <div class="field">Email</div>
    <div class="field tall">Message</div>
    <div class="submit">SUBMIT</div>
  </div>
  <div class="foot-brand"><div class="sq"></div><span>QUILL HARBOUR</span></div>
</footer>
<div class="copyright">Copyright © 2016 Quill Harbour. All rights reserved.</div>

</body>
</html>
```